Oregon Pawnbroker About Us Brochure

We need to make a front/back tri-fold "about us" informative brochure using the bullet points uploaded. Our association represents licensed pawnbrokers in the state of Oregon and this will be distributed to the entire legislative body in our state. I have attached our logo, but feel free to be creative with logo to enhance the overall appearance of the brochure.

Target Market(s)

Regulators and Politicians

Industry/Entity Type

Pawnbroker

Requirements
Must have
• Professional Appearance
Nice to have
• Graphics, color scheme

```html
<!DOCTYPE html>
<html lang="en">
<head>
<meta charset="utf-8">
<title>Cascade Pawn Alliance – Tri-fold Brochure</title>
<link href="https://fonts.googleapis.com/css2?family=Jost:wght@400;500;600&family=Open+Sans:ital,wght@0,400;0,600;1,400&display=swap" rel="stylesheet">
<style>
  :root{
    --navy:#3a3450;
    --lavender:#f4f3f9;
    --white:#ffffff;
    --ink:#3a3450;
    --body:#6a6778;
    --pink:#e0306a;
    --blue:#1aa3dc;
    --green:#1aa04a;
    --orange:#f5a623;
    --rule:#4a4a4a;
  }
  *{box-sizing:border-box;margin:0;padding:0}
  html,body{width:848px;height:1200px;overflow:hidden;background:var(--white)}
  body{position:relative;font-family:"Open Sans",Arial,sans-serif;color:var(--body)}

  .sheet{position:absolute;left:94px;width:659px;height:509px;border:1px solid var(--rule);background:var(--white);overflow:hidden;box-shadow:4px 4px 5px rgba(0,0,0,.35)}
  .sheet--outside{top:51px}
  .sheet--inside{top:639px}

  .panel{position:absolute;top:0;width:220px;height:100%}
  .panel--left{left:0;background:var(--white)}
  .panel--mid{left:219px;background:var(--lavender)}
  .panel--right{left:439px;width:220px;background:var(--white)}
  .panel--dark{background:var(--navy)}

  .photo{position:absolute;overflow:hidden}
  .photo svg{display:block;width:100%;height:100%}

  .eyebrow{position:absolute;font-size:5.6px;letter-spacing:.1px;text-transform:uppercase}
  .eyebrow--green{color:var(--green)}
  .eyebrow--blue{color:var(--blue)}
  .eyebrow--pink{color:var(--pink)}

  .heading{position:absolute;font-family:"Jost",Arial,sans-serif;font-weight:400;color:var(--ink);line-height:16px;font-size:13px;white-space:nowrap}
  .heading--light{color:var(--white)}

  /* about list */
  .point{position:absolute;left:23px;display:flex}
  .point__num{font-family:"Jost",Arial,sans-serif;font-size:20px;line-height:1;width:38px;flex:none}
  .point__text{font-size:6.6px;line-height:10px;padding-top:5px;width:136px}
  .num-pink{color:var(--pink)} .num-blue{color:var(--blue)} .num-green{color:var(--green)}

  /* contact card */
  .contact-card{position:absolute;left:24px;top:24px;width:172px;height:229px;background:var(--navy);border-radius:0 20px 0 20px}
  .contact-card .eyebrow{left:24px;top:41px}
  .contact-title{position:absolute;left:24px;top:48px;font-family:"Jost",Arial,sans-serif;font-weight:400;font-size:12.5px;color:var(--white)}
  .contact-title .accent{font-weight:500;text-decoration:underline wavy var(--pink);text-decoration-thickness:1px;text-underline-offset:2px}
  .contact-row{position:absolute;left:23px;display:flex;align-items:center;gap:10px}
  .contact-row__icon{width:19px;height:19px;border-radius:50%;background:var(--white);display:flex;align-items:center;justify-content:center;flex:none}
  .contact-row__text{font-size:6.6px;line-height:10px;color:#d8d6e2}

  /* support band */
  .support-band{position:absolute;left:24px;top:283px;width:196px;height:130px;background:var(--navy);border-radius:0 0 0 20px}
  .support-text{position:absolute;right:36px;top:20px;text-align:right;font-family:"Jost",Arial,sans-serif;font-weight:400;font-size:17.5px;line-height:20px;color:var(--white);white-space:nowrap}
  .support-text strong{font-weight:500;text-decoration:underline var(--green);text-decoration-thickness:1.5px;text-underline-offset:1px}
  .brand-seal{position:absolute;left:90px;top:351px;width:118px;height:118px;border-radius:50%;background:var(--white);border:1px solid #dcdce0;display:flex;align-items:center;justify-content:center;text-align:center}
  .brand-seal__name{font-family:"Jost",Arial,sans-serif;font-weight:500;font-size:10px;line-height:12px;color:var(--navy);width:80px}
  .dots-vertical{position:absolute;left:192px;top:466px;width:4px}
  .dots-vertical span{display:block;width:3px;height:3px;border-radius:50%;background:var(--green);margin-bottom:5px}

  /* bullet lists */
  .bullets{position:absolute;list-style:none;font-size:6.6px;line-height:10px}
  .bullets li{position:relative;padding-left:15px;margin-bottom:4px}
  .bullets li::before{content:"•";position:absolute;left:0;top:0;font-size:5px}
  .bullets--tight li{margin-bottom:0}
  .bullets .sub{list-style:none}
  .bullets .sub li{padding-left:15px;margin-bottom:0}
  .bullets--light{color:#d8d6e2}
  .bullets--light li{margin-bottom:7px}
  .lead{position:absolute;font-size:6.6px;line-height:10px}

  /* stats */
  .stat{position:absolute;border-radius:50%;background:var(--white);display:flex;flex-direction:column;align-items:center;justify-content:center;text-align:center;font-family:"Jost",Arial,sans-serif;color:var(--ink)}
  .stat__value{font-weight:500;line-height:1}
  .stat__label{line-height:1.2}
  .val-green{color:var(--green)} .val-pink{color:var(--pink)} .val-orange{color:var(--orange)} .val-blue{color:var(--blue)}
  .deco{position:absolute}
  .dot-grid{position:absolute;display:grid;gap:7px}
  .dot-grid span{width:2px;height:2px;border-radius:50%;background:#bdbbc8}
  .source{position:absolute;left:123px;top:491px;font-size:7.5px;font-style:italic;color:var(--body)}
</style>
</head>
<body>

<section class="sheet sheet--outside" aria-label="Brochure outside">
  <div class="panel panel--left">
    <div class="photo" style="left:24px;top:0;width:172px;height:97px;border-radius:0 0 20px 0" role="img" aria-label="Photo of a desk meeting with a calculator, small house model and paperwork">
      <svg viewBox="0 0 172 97" preserveAspectRatio="none"><defs><linearGradient id="g1" x1="0" y1="0" x2="1" y2="1"><stop offset="0" stop-color="#8a6a4c"/><stop offset=".55" stop-color="#c9b8a2"/><stop offset="1" stop-color="#5a4636"/></linearGradient></defs><rect width="172" height="97" fill="url(#g1)"/></svg>
    </div>
    <p class="eyebrow eyebrow--green" style="left:23px;top:131px">About us</p>
    <h2 class="heading" style="left:23px;top:139px">The Cascade Pawn<br>Alliance</h2>
    <div class="point" style="top:189px"><span class="point__num num-pink">01.</span><span class="point__text">United voice of Oregon Pawnbrokers</span></div>
    <div class="point" style="top:225px"><span class="point__num num-blue">02.</span><span class="point__text">Represents majority of pawnbrokers, both number of licensees and transactions processed.</span></div>
    <div class="point" style="top:269px"><span class="point__num num-green">03.</span><span class="point__text">Single point of contact for Oregon Legislature and all regulators to communicate with our industry.</span></div>
  </div>

  <div class="panel panel--mid">
    <div class="contact-card">
      <p class="eyebrow eyebrow--pink">Get in touch</p>
      <h2 class="contact-title">Contact Us <span class="accent">Now</span></h2>
      <div class="contact-row" style="top:110px">
        <span class="contact-row__icon"><svg width="10" height="10" viewBox="0 0 10 10"><path d="M5 9.5C5 9.5 1.8 6 1.8 3.9A3.2 3.2 0 0 1 8.2 3.9C8.2 6 5 9.5 5 9.5Z" fill="none" stroke="#e0306a" stroke-width=".8"/><circle cx="5" cy="4" r="1.1" fill="none" stroke="#e0306a" stroke-width=".8"/></svg></span>
        <span class="contact-row__text">Adress<br>Adress</span>
      </div>
      <div class="contact-row" style="top:140px">
        <span class="contact-row__icon"><svg width="10" height="10" viewBox="0 0 10 10"><rect x="1" y="2.2" width="8" height="5.6" fill="none" stroke="#e0306a" stroke-width=".8"/><path d="M1 2.2L5 5.6L9 2.2M1 7.8L4 5M9 7.8L6 5" fill="none" stroke="#e0306a" stroke-width=".7"/></svg></span>
        <span class="contact-row__text">contact@yourdomain.com<br>www.yourdomain.com</span>
      </div>
      <div class="contact-row" style="top:170px">
        <span class="contact-row__icon"><svg width="10" height="10" viewBox="0 0 10 10"><path d="M2.3 1.2L3.8 2.9L3 4.2C3.6 5.4 4.6 6.4 5.8 7L7.1 6.2L8.8 7.7L7.8 8.9C4.6 8.7 1.3 5.4 1.1 2.2Z" fill="none" stroke="#e0306a" stroke-width=".8" stroke-linejoin="round"/></svg></span>
        <span class="contact-row__text">Phone<br>Phone</span>
      </div>
    </div>
    <div class="photo" style="left:24px;top:277px;width:172px;height:208px;border-radius:20px 0 20px 0" role="img" aria-label="Photo of a smiling professional holding a laptop in an office">
      <svg viewBox="0 0 172 208" preserveAspectRatio="none"><defs><linearGradient id="g2" x1="0" y1="0" x2="1" y2="1"><stop offset="0" stop-color="#b59a82"/><stop offset=".5" stop-color="#c8d3e2"/><stop offset="1" stop-color="#8ea2bd"/></linearGradient></defs><rect width="172" height="208" fill="url(#g2)"/></svg>
    </div>
  </div>

  <div class="panel panel--right">
    <div class="photo" style="left:24px;top:0;width:196px;height:284px" role="img" aria-label="Photo of cash being handed over beside a laptop">
      <svg viewBox="0 0 196 284" preserveAspectRatio="none"><defs><linearGradient id="g3" x1="0" y1="0" x2="0" y2="1"><stop offset="0" stop-color="#cfd2cc"/><stop offset=".5" stop-color="#a9ae9f"/><stop offset="1" stop-color="#8a8778"/></linearGradient></defs><rect width="196" height="284" fill="url(#g3)"/></svg>
    </div>
    <div class="support-band">
      <p class="support-text">We <strong>Support</strong><br>local communities</p>
    </div>
    <div class="brand-seal"><span class="brand-seal__name">Cascade Pawn Alliance</span></div>
    <div class="dots-vertical"><span></span><span></span><span></span></div>
  </div>
</section>

<section class="sheet sheet--inside" aria-label="Brochure inside">
  <div class="panel panel--left">
    <h2 class="heading" style="left:23px;top:72px">Our Industry</h2>
    <ul class="bullets" style="left:23px;top:97px;width:172px">
      <li>Pawnbroking is the oldest form of regulated consumer credit.</li>
      <li>The Department of Consumer and Business Services issues the pawnbroker licenses here in Oregon.</li>
      <li>Currently, Oregon has 83 individually licensed pawnshops, 78 of which are brick-and-mortar, family-owned and operated businesses.</li>
      <li>Pawnbrokers offer highly regulated safety-net funds to consumers on a face-to-face basis from Main Street locations across the state.</li>
      <li>Lending decisions are solely based on the collateral and pawn transactions are non-recourse. No credit inquiries, No credit reporting, No collections, No cycle of debt.</li>
      <li>Pawnbrokers provide safe, secure storage for items customers cannot or do not want to store themselves, including oversized or seasonal items construction equipment, and firearms.</li>
    </ul>
    <div class="photo" style="left:24px;top:310px;width:172px;height:175px;border-radius:20px 0 20px 0" role="img" aria-label="Photo of a hand pressing an official rubber stamp">
      <svg viewBox="0 0 172 175" preserveAspectRatio="none"><defs><radialGradient id="g4" cx=".45" cy=".4" r=".75"><stop offset="0" stop-color="#c08d6e"/><stop offset=".5" stop-color="#8a7468"/><stop offset="1" stop-color="#1e2426"/></radialGradient></defs><rect width="172" height="175" fill="url(#g4)"/></svg>
    </div>
  </div>

  <div class="panel panel--mid">
    <p class="eyebrow eyebrow--blue" style="left:24px;top:63px">Our experience</p>
    <h2 class="heading" style="left:24px;top:72px">Regulations</h2>
    <p class="lead" style="left:24px;top:97px;width:176px">Pawnshops are heavily regulated and work closely with the federal, state and local governments and law enforcement.</p>
    <ul class="bullets bullets--tight" style="left:24px;top:127px;width:182px">
      <li>ORS 726 and OAR 441-740 define the requirements for our industry here in Oregon including the requirements of a loan, duration of a loan, as well as the interest and fees charged.</li>
      <li>Transactions require customer to present government issued photo identification.</li>
      <li>All transactions are reported daily to law enforcement.</li>
      <li>Oregon Pawnbrokers work closely with the following regulators:
        <ul class="sub">
          <li>Department of Consumer and Business Services</li>
          <li>Bureau of Alcohol Tobacco and Firearms</li>
          <li>State Police</li>
          <li>Department of Agriculture</li>
        </ul>
      </li>
    </ul>

    <div class="stat" style="left:24px;top:278px;width:94px;height:94px">
      <span class="stat__value val-green" style="font-size:25px">$175</span>
      <span class="stat__label" style="font-size:8px">Average loan<br>amount in 2020</span>
    </div>
    <div class="stat" style="left:133px;top:302px;width:64px;height:64px">
      <span class="stat__value val-pink" style="font-size:16px">72%</span>
      <span class="stat__label" style="font-size:6px">Redemption<br>rate</span>
    </div>
    <div class="stat" style="left:24px;top:398px;width:62px;height:62px">
      <span class="stat__value val-orange" style="font-size:15px">0.085%</span>
      <span class="stat__label" style="font-size:6px">Police pickup<br>rate</span>
    </div>
    <div class="stat" style="left:103px;top:391px;width:92px;height:92px">
      <span class="stat__value val-blue" style="font-size:11.5px;margin-bottom:4px">206,500</span>
      <span class="stat__label" style="font-size:7.6px">Number of loans made<br>by Oregon pawnshops<br>in 2020, lending $33.2<br>million to customers.</span>
    </div>

    <svg class="deco" style="left:123px;top:288px" width="12" height="12" viewBox="0 0 12 12" aria-hidden="true"><path d="M2 2L10 10M10 2L2 10" stroke="#f08aa8" stroke-width="2.6" stroke-linecap="round"/></svg>
    <svg class="deco" style="left:24px;top:369px" width="12" height="12" viewBox="0 0 12 12" aria-hidden="true"><path d="M6 1L11 6L6 11L1 6Z" fill="none" stroke="#a8dcf0" stroke-width="1"/></svg>
    <svg class="deco" style="left:80px;top:466px" width="22" height="19" viewBox="0 0 22 19" aria-hidden="true"><path d="M11 0L22 19H0Z" fill="#f8b133"/></svg>
    <div class="dot-grid" style="left:89px;top:381px;grid-template-columns:repeat(5,2px)">
      <span></span><span></span><span></span><span></span><span></span>
      <span></span><span></span><span></span><span></span><span></span>
      <span></span><span></span><span></span><span></span><span></span>
    </div>
    <div class="dot-grid" style="left:89px;top:408px;grid-template-columns:2px">
      <span></span><span></span><span></span><span></span><span></span>
    </div>
    <p class="source">Reported by DCBS</p>
  </div>

  <div class="panel panel--right panel--dark">
    <p class="eyebrow eyebrow--pink" style="left:24px;top:63px">The service</p>
    <h2 class="heading heading--light" style="left:24px;top:72px">Why Pawnbrokers are Important<br>to Oregon Consumers</h2>
    <ul class="bullets bullets--light" style="left:24px;top:113px;width:178px">
      <li>Without state-licensed pawnbrokers, Oregonians could be forced to borrow from unlicensed people with unregulated loans that include very high interest rates or instead, forced to sell their property entirely, diminishing their personal assets.</li>
      <li>Other credit based lenders, such as banks and credit unions, do not offer Oregonians loan products at the small dollar amounts our industry serves.</li>
      <li>Pawnbrokers provide a same day financial solution.</li>
      <li>Pawnbrokers are invested in our communities and are sensitive to the needs of our customers.</li>
    </ul>
    <div class="photo" style="left:24px;top:310px;width:196px;height:175px;border-radius:0 0 0 20px" role="img" aria-label="Photo of cash passed across a counter window">
      <svg viewBox="0 0 196 175" preserveAspectRatio="none"><defs><linearGradient id="g5" x1="0" y1="0" x2="1" y2="1"><stop offset="0" stop-color="#d9b889"/><stop offset=".45" stop-color="#eeeeec"/><stop offset="1" stop-color="#b9b7b2"/></linearGradient></defs><rect width="196" height="175" fill="url(#g5)"/></svg>
    </div>
  </div>
</section>

</body>
</html>
```